New Plumbing Company

We are looking for a smart and creative business card design for our new plumbing company. We are looking for creativity and originality in our business cards.

Industry/Entity Type

Plumbing

Contact Information for Business Card

Crestline Plumbing
Peter Halvane
Managing Director
Telephone Number : 0481529604
Email : service@crestlineplumbing.com.au
Website : www.crestlineplumbing.com.au
Lic. 508264K

Colors
0692cd
33a6d7
000000

Requirements
Must have
• I want the business card to be designed on a black background using the blue tones i have selected as seen in the company logo.

```html
<!DOCTYPE html>
<html lang="en">
<head>
<meta charset="utf-8">
<title>Crestline Plumbing – Business Card</title>
<link rel="stylesheet" href="https://fonts.googleapis.com/css2?family=Open+Sans:wght@400;600&family=Roboto:wght@400;900&display=swap">
<style>
  :root {
    --page-bg: #e6e6e4;
    --card-top: #2c3234;
    --card-bottom: #1f2426;
    --brand-blue: #3b7fd4;
    --brand-sky: #33a6d7;
    --rule: #3a4b60;
    --text-light: #dcdcdc;
    --text-white: #ffffff;
  }
  * { margin: 0; padding: 0; box-sizing: border-box; }
  html, body {
    width: 1200px; height: 800px; overflow: hidden;
    background: var(--page-bg);
  }
  .stage {
    width: 1200px; height: 800px;
    display: flex; align-items: center; justify-content: center;
  }
  .business-card {
    position: relative;
    width: 900px; height: 515px;
    background: linear-gradient(180deg, var(--card-top), var(--card-bottom));
    box-shadow: 0 10px 30px rgba(0,0,0,0.25);
    overflow: hidden;
  }
  .holder-name {
    position: absolute; left: 62px; top: 62px;
    font-family: "Roboto", Arial, sans-serif;
    font-weight: 900; font-size: 34px; letter-spacing: 5px;
    color: var(--brand-blue);
  }
  .header-rule {
    position: absolute; left: 0; right: 0; top: 126px;
    height: 2px; background: var(--rule);
  }
  .holder-title {
    position: absolute; left: 88px; top: 158px;
    font-family: "Roboto", Arial, sans-serif;
    font-size: 21px; letter-spacing: 4px;
    color: var(--text-light);
  }
  .contact-list {
    position: absolute; left: 34px; top: 250px;
    list-style: none;
    font-family: "Open Sans", Arial, sans-serif;
    font-size: 19px; color: var(--text-light);
  }
  .contact-item {
    display: flex; align-items: center;
    height: 38px;
  }
  .contact-icon {
    width: 22px; height: 22px; margin-right: 30px;
    flex: none;
  }
  .brand-mark {
    position: absolute; left: 520px; top: 262px;
    display: flex; align-items: center; gap: 22px;
  }
  .brand-dot {
    width: 92px; height: 92px; border-radius: 50%;
    border: 4px solid var(--brand-blue);
  }
  .brand-name {
    font-family: "Open Sans", Arial, sans-serif;
    font-weight: 400; font-size: 34px; line-height: 1.1;
    color: var(--text-white);
  }
</style>
</head>
<body>
<main class="stage">
  <section class="business-card">
    <h1 class="holder-name">Peter Halvane</h1>
    <div class="header-rule"></div>
    <p class="holder-title">Managing Director</p>

    <ul class="contact-list">
      <li class="contact-item">
        <svg class="contact-icon" viewBox="0 0 24 24" aria-hidden="true">
          <circle cx="12" cy="12" r="10" fill="var(--brand-blue)"/>
          <path d="M6 9c2-1 3 1 5 0s1-3 3-3M9 16c1-2 3-1 4-3s3-1 4 1" stroke="#1f2426" stroke-width="1.6" fill="none"/>
        </svg>
        <span>www.crestlineplumbing.com.au</span>
      </li>
      <li class="contact-item">
        <svg class="contact-icon" viewBox="0 0 24 24" aria-hidden="true">
          <path d="M7 3h4l1 5-3 2c1 2 3 4 5 5l2-3 5 1v4c0 1-1 2-2 2C10 19 5 14 5 5c0-1 1-2 2-2z" fill="var(--brand-blue)"/>
        </svg>
        <span>0481529604</span>
      </li>
      <li class="contact-item">
        <svg class="contact-icon" viewBox="0 0 24 24" aria-hidden="true">
          <rect x="6" y="3" width="12" height="7" fill="none" stroke="var(--brand-blue)" stroke-width="2"/>
          <rect x="3" y="10" width="18" height="8" fill="var(--brand-blue)"/>
          <rect x="6" y="15" width="12" height="6" fill="none" stroke="var(--brand-blue)" stroke-width="2"/>
        </svg>
        <span>0481529604</span>
      </li>
      <li class="contact-item">
        <svg class="contact-icon" viewBox="0 0 24 24" aria-hidden="true">
          <rect x="2" y="5" width="20" height="14" fill="none" stroke="var(--brand-blue)" stroke-width="2"/>
          <path d="M2 5l10 8 10-8" fill="none" stroke="var(--brand-blue)" stroke-width="2"/>
        </svg>
        <span>service@crestlineplumbing.com.au</span>
      </li>
    </ul>

    <div class="brand-mark">
      <div class="brand-dot"></div>
      <p class="brand-name">Crestline Plumbing</p>
    </div>
  </section>
</main>
</body>
</html>
```